Email Signatures

I would like to create a new email signature for my team. The design will be the same for everyone, with only individual details such as name and email changing. You can also see our brand style on our website. https://www.tlmbespokehomes.com.au/

Target Market(s)

Clients for new builds or renovations

Industry/Entity Type

Construction

Colors

Designer to choose colors to be used in the design.

```html
<!DOCTYPE html>
<html lang="en">
<head>
<meta charset="utf-8">
<title>TLM Email Signature</title>
<link rel="stylesheet" href="https://fonts.googleapis.com/css2?family=Arimo:wght@400;700&display=swap">
<style>
  :root {
    --page-bg: #d4d5d7;
    --navy: #243142;
    --navy-icon: #1f2b3a;
    --green-dark: #5db544;
    --green-light: #8fd160;
    --name-green: #5cb946;
    --white: #ffffff;
    --photo-tone: #3d5667;
  }
  html, body {
    margin: 0;
    width: 1200px;
    height: 600px;
    overflow: hidden;
    background: var(--page-bg);
  }
  .canvas {
    position: relative;
    width: 1200px;
    height: 600px;
  }
  .signature {
    position: absolute;
    left: 210px;
    width: 778px;
    height: 259px;
    display: block;
  }
  .signature--house { top: 19px; }
  .signature--portrait { top: 310px; }
  .brand-name {
    font-family: "Arimo", Arial, sans-serif;
    font-weight: 700;
    font-size: 96px;
    fill: var(--white);
    letter-spacing: 2px;
  }
  .person-name {
    font-family: "Arimo", Arial, sans-serif;
    font-weight: 700;
    font-size: 52px;
    fill: var(--name-green);
  }
  .person-role {
    font-family: "Arimo", Arial, sans-serif;
    font-weight: 400;
    font-size: 35px;
    fill: var(--white);
    letter-spacing: 0.5px;
  }
  .contact-text {
    font-family: "Arimo", Arial, sans-serif;
    font-weight: 400;
    font-size: 23px;
    fill: var(--white);
  }
  .contact-badge { fill: var(--name-green); }
  .contact-glyph { fill: var(--navy-icon); }
  .contact-line { fill: none; stroke: var(--navy-icon); stroke-width: 1.8; }
  .social-dot { fill: var(--name-green); }
  .band-light { fill: var(--green-light); }
  .band-dark { fill: var(--green-dark); }
  .frame { fill: var(--white); }
  .base { fill: var(--navy); }
</style>
</head>
<body>
<div class="canvas">

  <!-- Signature with house image -->
  <svg class="signature signature--house" viewBox="0 0 1670 557" xmlns="http://www.w3.org/2000/svg">
    <defs>
      <linearGradient id="backdrop-tone" x1="0" y1="0" x2="1" y2="0.3">
        <stop offset="0" stop-color="#243142"/>
        <stop offset="0.45" stop-color="#2f4455"/>
        <stop offset="1" stop-color="#3f5b6c"/>
      </linearGradient>
      <linearGradient id="house-tone" x1="0" y1="0" x2="0" y2="1">
        <stop offset="0" stop-color="#1e2d45"/>
        <stop offset="0.5" stop-color="#6b5a45"/>
        <stop offset="1" stop-color="#3a342e"/>
      </linearGradient>
      <linearGradient id="portrait-tone" x1="0" y1="0" x2="0" y2="1">
        <stop offset="0" stop-color="#f1f1f1"/>
        <stop offset="0.55" stop-color="#e4c2ad"/>
        <stop offset="1" stop-color="#2b2f36"/>
      </linearGradient>
    </defs>

    <rect class="base" width="1670" height="557"/>
    <polygon points="900,0 1670,0 1670,557 650,557" fill="url(#backdrop-tone)" role="img" aria-label="Photo of rolled construction blueprints on a desk"/>

    <!-- left ribbon -->
    <path class="band-light" d="M0,390 L318,72 Q333,57 355,57 L512,57 L14,557 L0,557 Z"/>
    <path class="band-dark" d="M420,57 L512,57 L14,557 L0,557 L0,477 Z"/>

    <!-- right ribbon -->
    <path class="band-dark" d="M1012,0 L1190,0 L700,490 Q688,502 668,502 L512,502 Z"/>
    <path class="band-light" d="M1100,0 L1190,0 L700,490 Q688,502 668,502 L598,502 Z"/>

    <!-- corner accent -->
    <polygon class="band-light" points="1500,557 1670,387 1670,557"/>
    <polygon class="band-dark" points="1590,557 1670,477 1670,557"/>

    <!-- framed image -->
    <polygon class="frame" points="512,57 735,281 512,502 290,281"/>
    <polygon points="512,88 705,281 512,472 320,281" fill="url(#house-tone)" role="img" aria-label="Photo of a modern two-storey home lit at dusk"/>

    <!-- brand -->
    <text class="brand-name" x="48" y="125">TLM</text>

    <!-- social -->
    <circle class="social-dot" cx="188" cy="481" r="23"/>
    <circle class="social-dot" cx="259" cy="481" r="23"/>
    <circle class="social-dot" cx="330" cy="481" r="23"/>
    <circle class="social-dot" cx="401" cy="481" r="23"/>

    <!-- details -->
    <text class="person-name" x="1080" y="192">LIAM CARTER</text>
    <text class="person-role" x="1092" y="243">GENERAL MANAGER</text>

    <circle class="contact-badge" cx="1101" cy="316" r="15"/>
    <path class="contact-glyph" d="M1101,307 L1109,315 L1106,315 L1106,323 L1096,323 L1096,315 L1093,315 Z"/>
    <text class="contact-text" x="1132" y="324">Launceston, Tasmania, Australia</text>

    <circle class="contact-badge" cx="1101" cy="362" r="15"/>
    <path class="contact-glyph" d="M1095,355 Q1097,353 1099,355 L1101,359 Q1101,361 1099,362 Q1101,366 1104,367 Q1105,365 1107,365 L1110,367 Q1111,369 1109,371 Q1105,373 1099,368 Q1093,362 1095,355 Z"/>
    <text class="contact-text" x="1132" y="370">0400 555 018</text>

    <circle class="contact-badge" cx="1101" cy="408" r="15"/>
    <rect class="contact-glyph" x="1093" y="402" width="16" height="12" rx="1"/>
    <path class="contact-line" stroke="#5cb946" d="M1093,403 L1101,409 L1109,403" style="stroke:#5cb946"/>
    <text class="contact-text" x="1132" y="416">info@tlmbespokehomes.com.au</text>

    <circle class="contact-badge" cx="1101" cy="453" r="15"/>
    <circle class="contact-line" cx="1101" cy="453" r="7.5"/>
    <ellipse class="contact-line" cx="1101" cy="453" rx="3.2" ry="7.5"/>
    <path class="contact-line" d="M1093.5,453 L1108.5,453"/>
    <text class="contact-text" x="1132" y="461">https://www.tlmbespokehomes.com.au</text>
  </svg>

  <!-- Signature with portrait -->
  <svg class="signature signature--portrait" viewBox="0 0 1670 557" xmlns="http://www.w3.org/2000/svg">
    <rect class="base" width="1670" height="557"/>
    <polygon points="900,0 1670,0 1670,557 650,557" fill="url(#backdrop-tone)" role="img" aria-label="Photo of rolled construction blueprints on a desk"/>

    <path class="band-light" d="M0,390 L318,72 Q333,57 355,57 L512,57 L14,557 L0,557 Z"/>
    <path class="band-dark" d="M420,57 L512,57 L14,557 L0,557 L0,477 Z"/>

    <path class="band-dark" d="M1012,0 L1190,0 L700,490 Q688,502 668,502 L512,502 Z"/>
    <path class="band-light" d="M1100,0 L1190,0 L700,490 Q688,502 668,502 L598,502 Z"/>

    <polygon class="band-light" points="1500,557 1670,387 1670,557"/>
    <polygon class="band-dark" points="1590,557 1670,477 1670,557"/>

    <polygon class="frame" points="512,57 735,281 512,502 290,281"/>
    <polygon points="512,88 705,281 512,472 320,281" fill="url(#portrait-tone)" role="img" aria-label="Portrait photo of the team member"/>

    <text class="brand-name" x="48" y="125">TLM</text>

    <circle class="social-dot" cx="188" cy="481" r="23"/>
    <circle class="social-dot" cx="259" cy="481" r="23"/>
    <circle class="social-dot" cx="330" cy="481" r="23"/>
    <circle class="social-dot" cx="401" cy="481" r="23"/>

    <text class="person-name" x="1080" y="192">LIAM CARTER</text>
    <text class="person-role" x="1092" y="243">GENERAL MANAGER</text>

    <circle class="contact-badge" cx="1101" cy="316" r="15"/>
    <path class="contact-glyph" d="M1101,307 L1109,315 L1106,315 L1106,323 L1096,323 L1096,315 L1093,315 Z"/>
    <text class="contact-text" x="1132" y="324">Launceston, Tasmania, Australia</text>

    <circle class="contact-badge" cx="1101" cy="362" r="15"/>
    <path class="contact-glyph" d="M1095,355 Q1097,353 1099,355 L1101,359 Q1101,361 1099,362 Q1101,366 1104,367 Q1105,365 1107,365 L1110,367 Q1111,369 1109,371 Q1105,373 1099,368 Q1093,362 1095,355 Z"/>
    <text class="contact-text" x="1132" y="370">0400 555 018</text>

    <circle class="contact-badge" cx="1101" cy="408" r="15"/>
    <rect class="contact-glyph" x="1093" y="402" width="16" height="12" rx="1"/>
    <path class="contact-line" d="M1093,403 L1101,409 L1109,403" style="stroke:#5cb946"/>
    <text class="contact-text" x="1132" y="416">info@tlmbespokehomes.com.au</text>

    <circle class="contact-badge" cx="1101" cy="453" r="15"/>
    <circle class="contact-line" cx="1101" cy="453" r="7.5"/>
    <ellipse class="contact-line" cx="1101" cy="453" rx="3.2" ry="7.5"/>
    <path class="contact-line" d="M1093.5,453 L1108.5,453"/>
    <text class="contact-text" x="1132" y="461">https://www.tlmbespokehomes.com.au</text>
  </svg>

</div>
</body>
</html>
```